Tarn Business Card Design Project

We have an existing business card. We are looking to creat a new card for the store. I have attached a my own business so you have a refference of what the current card looks like.

Phone: 1300 571 342
email: kelwood@tarnglazing.com.au
website: www.tarnglazing.com.au
Address: (Inside Kelwood Flooring Yard) 214 Farrow Rd, Hughesdale VIC 3166
Updates

This is a new business card for our store.

Industry/Entity Type

Business

Requirements
Must have
• Must look similar to the existing card

```html
<!DOCTYPE html>
<html lang="en">
<head>
<meta charset="utf-8">
<title>Tarn Shutters &amp; Blinds — Business Card</title>
<link href="https://fonts.googleapis.com/css2?family=Exo+2:wght@300;400;600&family=Michroma&display=swap" rel="stylesheet">
<style>
  :root{
    --bg:#8a8a8a;
    --card-white:#f4f4f4;
    --band-grey:#6e6e6e;
    --panel-dark:#262626;
    --panel-dark-2:#353535;
    --pill:#d9d9d9;
    --pill-edge:#eeeeee;
    --ink:#3a3a3a;
    --tagline:#8c8c8c;
    --white:#ffffff;
    --rule:#bdbdbd;
  }
  *{box-sizing:border-box;margin:0;padding:0}
  html,body{width:1200px;height:897px;overflow:hidden}
  body{background:var(--bg);position:relative;font-family:"Exo 2",sans-serif}

  .card{position:absolute;top:118px;width:340px;height:660px;overflow:hidden;border-radius:4px;box-shadow:0 10px 28px rgba(0,0,0,.35)}
  .card--front{left:200px;background:var(--card-white)}
  .card--back{left:660px;background:linear-gradient(160deg,var(--panel-dark-2),var(--panel-dark) 70%)}

  .card__shapes{position:absolute;inset:0}

  .brand{position:absolute;left:70px;top:58px}
  .brand__name{font-family:"Exo 2",sans-serif;font-weight:300;font-size:76px;line-height:1;color:var(--ink);letter-spacing:1px}
  .brand__tagline{font-family:"Exo 2",sans-serif;font-weight:600;font-size:17px;color:var(--tagline);margin-top:2px;margin-left:6px}

  .person{position:absolute;left:70px;top:298px;color:var(--white)}
  .person__name{font-family:"Michroma",sans-serif;font-size:21px;letter-spacing:1px;line-height:1}
  .person__role{font-family:"Michroma",sans-serif;font-size:9.5px;letter-spacing:1.5px;margin-top:6px}

  .address{position:absolute;left:44px;top:356px;width:272px;height:52px;border-radius:10px;background:linear-gradient(var(--pill-edge),var(--pill));display:flex;align-items:center;padding:0 14px;font-size:14px;line-height:1.2;color:var(--ink)}

  .contacts{position:absolute;left:80px;top:424px;width:210px;list-style:none;color:var(--white);text-align:center}
  .contact{position:relative;height:50px;display:flex;flex-direction:column;align-items:center;justify-content:flex-end;padding-bottom:6px;font-size:12.5px;letter-spacing:.5px}
  .contact__icon{position:absolute;top:4px;left:50%;transform:translateX(-50%);width:14px;height:14px;background:var(--panel-dark);padding:0 2px;box-sizing:content-box}
  .contact__rule{position:absolute;top:11px;left:0;right:0;height:1px;background:var(--rule)}
  .contact__icon svg{display:block;width:14px;height:14px}

  .brand--back{left:74px;top:118px}
  .brand--back .brand__name{color:var(--white)}
  .brand--back .brand__tagline{color:#a8a8a8}

  .web-pill{position:absolute;left:22px;top:584px;width:296px;height:50px;border-radius:12px;background:linear-gradient(var(--pill-edge),var(--pill));display:flex;align-items:center;justify-content:flex-end;padding-right:18px;font-size:15px;color:var(--ink)}
</style>
</head>
<body>

<section class="card card--front" aria-label="Business card front">
  <svg class="card__shapes" width="340" height="660" viewBox="0 0 340 660" aria-hidden="true">
    <path d="M0 262 Q150 200 340 212 L340 660 L0 660 Z" fill="var(--band-grey)"/>
    <path d="M22 660 L22 320 Q22 262 90 258 Q210 248 340 246 L340 660 Z" fill="var(--panel-dark)"/>
  </svg>

  <div class="brand">
    <div class="brand__name">Tarn</div>
    <div class="brand__tagline">Shutters &amp; Blinds</div>
  </div>

  <div class="person">
    <div class="person__name">MARA KELLER</div>
    <div class="person__role">GENERAL MANAGER</div>
  </div>

  <div class="address">Kelwood Flooring Yard<br>214 Farrow Rd</div>

  <ul class="contacts">
    <li class="contact">
      <span class="contact__rule"></span>
      <span class="contact__icon"><svg viewBox="0 0 24 24"><path fill="#fff" d="M6.6 10.8a15 15 0 0 0 6.6 6.6l2.2-2.2c.3-.3.7-.4 1-.2 1.1.4 2.3.6 3.6.6.6 0 1 .4 1 1V20c0 .6-.4 1-1 1A17 17 0 0 1 3 4c0-.6.4-1 1-1h3.5c.6 0 1 .4 1 1 0 1.3.2 2.5.6 3.6.1.3 0 .7-.2 1z"/></svg></span>
      <span>1300 571 342</span>
    </li>
    <li class="contact">
      <span class="contact__rule"></span>
      <span class="contact__icon"><svg viewBox="0 0 24 24"><rect x="6" y="2" width="12" height="20" rx="2" fill="none" stroke="#fff" stroke-width="2"/><circle cx="12" cy="18" r="1.3" fill="#fff"/></svg></span>
      <span>1300 571 342</span>
    </li>
    <li class="contact">
      <span class="contact__rule"></span>
      <span class="contact__icon"><svg viewBox="0 0 24 24"><rect x="2" y="5" width="20" height="14" rx="1.5" fill="#fff"/><path d="M2 6l10 7 10-7" fill="none" stroke="#262626" stroke-width="1.6"/></svg></span>
      <span>kelwood@tarnglazing.com.au</span>
    </li>
    <li class="contact">
      <span class="contact__rule"></span>
      <span class="contact__icon"><svg viewBox="0 0 24 24"><g fill="none" stroke="#fff" stroke-width="1.8"><circle cx="12" cy="12" r="9.5"/><ellipse cx="12" cy="12" rx="4" ry="9.5"/><path d="M2.5 12h19M4 7h16M4 17h16"/></g></svg></span>
      <span>www.tarnglazing.com.au</span>
    </li>
  </ul>
</section>

<section class="card card--back" aria-label="Business card back">
  <div class="brand brand--back">
    <div class="brand__name">Tarn</div>
    <div class="brand__tagline">Shutters &amp; Blinds</div>
  </div>
  <div class="web-pill">www.tarnglazing.com.au</div>
</section>

</body>
</html>
```